Infographics about Quarnel Census

Hello, we are Plenvoria, a leading Big Data and Data Science consultancy firm from The Netherlands. We are looking for an awesome infographic.

Introduction
In order to create a better understanding of the status of Big Data in our little country, together with the biggest Big Data trade show Quarnel Fair, we created the Quarnel Census. This first national research on Big Data aims at providing insight in use of Big Data. The survey is built on five corner stones: Organization, Data, Technology, Skills and Process.

Design
We are looking for an insightful representation of the key-results of the survey, based on the five corner stones. It may also very well be multiple infographics in order to decrease the information density, but I'll leave that to you.

We are looking for a fresh, funky and attractive design, that is easily understood. Please use the colors (orange and blue) of the survey report. For more information see: http://www.plenvoria-example.com/static/images/quarnelcensus/quarnelcensus-uitkomst-web.pdf

```html
<!DOCTYPE html>
<html lang="en">
<head>
<meta charset="utf-8">
<title>Quarnel Census – Process</title>
<link rel="stylesheet" href="https://fonts.googleapis.com/css2?family=Oswald:wght@300;400&family=Roboto+Condensed:wght@300;400&display=swap">
<style>
  :root {
    --orange: #f7931e;
    --blue-deep: #2e6da4;
    --blue-light: #4b94d2;
    --tower: #4a4a4a;
    --stair: #333333;
    --paper: #ffffff;
    --ink: #3a3a3a;
    --screen: #f4a64c;
    --frame: #5a5a5a;
  }
  * { box-sizing: border-box; margin: 0; padding: 0; }
  html, body { width: 1200px; height: 3228px; overflow: hidden; background: var(--paper); }
  body { position: relative; font-family: "Roboto Condensed", Arial, sans-serif; color: var(--paper); }
  .band { position: absolute; left: 0; width: 1200px; }
  .band > svg { position: absolute; left: 0; top: 0; }
  .top-bar { top: 0; height: 91px; background: var(--orange); }
  .top-bar h1 { font-family: "Oswald", sans-serif; font-weight: 400; font-size: 40px; line-height: 91px; text-align: center; letter-spacing: 1px; }
  .ethics { top: 91px; height: 713px; background: var(--blue-deep); }
  .personalize { top: 804px; height: 956px; background: var(--blue-light); }
  .usage { top: 1760px; height: 628px; background: var(--blue-deep); }
  .advanced { top: 2388px; height: 564px; background: var(--blue-light); }
  .footer { top: 2952px; height: 240px; background: var(--paper); }
  .bottom-bar { top: 3192px; height: 36px; background: var(--orange); }
  .section-title { position: absolute; left: 0; width: 1200px; text-align: center; font-family: "Oswald", sans-serif; font-weight: 300; font-size: 38px; line-height: 54px; }
  .badge { position: absolute; width: 74px; height: 74px; border-radius: 50%; background: var(--orange); font-family: "Oswald", sans-serif; font-weight: 300; font-size: 27px; line-height: 74px; text-align: center; }
  .caption { position: absolute; text-align: center; font-size: 30px; line-height: 38px; font-weight: 300; }
  .personalize .caption, .advanced .caption { color: #eef5fc; }
  .stair-label { position: absolute; text-align: center; font-size: 28px; line-height: 32px; font-weight: 300; }
  .stair-value { position: absolute; text-align: center; font-size: 27px; font-weight: 300; }
  .group-label { position: absolute; font-size: 30px; font-weight: 400; }
  .brand { position: absolute; top: 100px; display: flex; align-items: center; gap: 16px; font-family: "Roboto Condensed", sans-serif; font-weight: 400; font-size: 40px; color: var(--ink); }
  .brand-mark { width: 34px; height: 34px; background: var(--blue-deep); }
</style>
</head>
<body>

<header class="band top-bar"><h1>PROCESS</h1></header>

<section class="band ethics">
  <h2 class="section-title" style="top:0">1. Data Ethics and Value</h2>
  <svg width="1200" height="713" viewBox="0 0 1200 713">
    <rect x="168" y="137" width="115" height="305" fill="var(--tower)" role="img" aria-label="Office tower showing consumer awareness split"/>
    <rect x="547" y="96" width="101" height="269" fill="var(--tower)" role="img" aria-label="Office tower showing ethical responsibility split"/>
    <rect x="912" y="137" width="91" height="305" fill="var(--tower)" role="img" aria-label="Office tower showing data as currency split"/>
    <g stroke="#fff" stroke-width="3" stroke-dasharray="12 8" fill="none">
      <line x1="72" y1="420" x2="300" y2="420"/>
      <line x1="432" y1="173" x2="684" y2="173"/>
      <line x1="828" y1="197" x2="1056" y2="197"/>
    </g>
    <g stroke="#fff" stroke-width="3" fill="none">
      <path d="M282 425 C 305 450, 305 480, 300 515"/><path d="M288 502 L300 517 L312 502"/>
      <path d="M530 345 C 505 380, 490 400, 495 430"/><path d="M483 418 L495 432 L507 418"/>
      <path d="M925 445 C 905 470, 898 495, 900 520"/><path d="M888 507 L900 522 L912 507"/>
    </g>
  </svg>
  <div class="badge" style="left:78px;top:323px">90%</div>
  <div class="badge" style="left:78px;top:429px">10%</div>
  <div class="badge" style="left:462px;top:88px">18%</div>
  <div class="badge" style="left:462px;top:189px">82%</div>
  <div class="badge" style="left:822px;top:119px">1/3</div>
  <div class="badge" style="left:822px;top:208px">2/3</div>
  <p class="caption" style="left:20px;top:533px;width:420px">Only 10% of participants think that consumers are well aware of the data trail they are leaving behind.</p>
  <p class="caption" style="left:395px;top:430px;width:410px">Luckily, 82% of participants agrees that companies are responsible for collecting data ethically.</p>
  <p class="caption" style="left:790px;top:533px;width:410px">Two third of all participants expects that in the future consumers can use data as a form of currency.</p>
</section>

<section class="band personalize">
  <h2 class="section-title" style="top:14px">2. To What Extent Do You Personalize Your Website?</h2>
  <svg width="1200" height="956" viewBox="0 0 1200 956">
    <rect x="163" y="168" width="233" height="216" fill="var(--frame)" role="img" aria-label="Browser window with a static page"/>
    <rect x="715" y="156" width="336" height="228" fill="var(--frame)" role="img" aria-label="Laptop showing code"/>
    <rect x="221" y="576" width="163" height="252" fill="#fbe08f" role="img" aria-label="Sheet of historical data"/>
    <rect x="763" y="600" width="274" height="209" fill="var(--frame)" role="img" aria-label="Dashboard with live charts"/>
    <line x1="72" y1="761" x2="492" y2="761" stroke="#fff" stroke-width="3" stroke-dasharray="12 8"/>
  </svg>
  <div class="badge" style="left:143px;top:66px">54%</div>
  <div class="badge" style="left:241px;top:66px">46%</div>
  <div class="badge" style="left:681px;top:66px">29%</div>
  <div class="badge" style="left:777px;top:66px">71%</div>
  <div class="badge" style="left:131px;top:671px">85%</div>
  <div class="badge" style="left:131px;top:772px">15%</div>
  <div class="badge" style="left:705px;top:515px">11%</div>
  <div class="badge" style="left:801px;top:515px">89%</div>
  <p class="caption" style="left:88px;top:425px;width:400px">46% does not personalize its website</p>
  <p class="caption" style="left:683px;top:425px;width:400px">29% does this manually</p>
  <p class="caption" style="left:88px;top:857px;width:400px">15% personalizes based on historical data</p>
  <p class="caption" style="left:680px;top:833px;width:440px">11% is able to personalize the website in real-time based on current visitor behavior</p>
</section>

<section class="band usage">
  <h2 class="section-title" style="top:0">3. What Do You Use Data For?</h2>
  <p class="group-label" style="left:310px;top:140px">Bottom 3</p>
  <p class="group-label" style="left:780px;top:140px">Top 3</p>
  <svg width="1200" height="628" viewBox="0 0 1200 628">
    <path d="M108 592 V532 H269 V472 H432 V412 H600 V352 H768 V292 H931 V232 H1099 V592 Z" fill="var(--stair)"/>
    <line x1="600" y1="148" x2="600" y2="604" stroke="#fff" stroke-width="3" stroke-dasharray="12 8"/>
  </svg>
  <p class="stair-label" style="left:108px;top:488px;width:130px">HR</p>
  <p class="stair-label" style="left:240px;top:396px;width:200px">Finance and<br>Administration</p>
  <p class="stair-label" style="left:410px;top:330px;width:180px">Supply Chain<br>&amp; Logistics</p>
  <p class="stair-label" style="left:600px;top:272px;width:168px">Market<br>Analysis</p>
  <p class="stair-label" style="left:768px;top:244px;width:163px">Online</p>
  <p class="stair-label" style="left:931px;top:186px;width:168px">Marketing</p>
  <p class="stair-value" style="left:108px;top:548px;width:150px">3%</p>
  <p class="stair-value" style="left:269px;top:488px;width:150px">4%</p>
  <p class="stair-value" style="left:432px;top:428px;width:150px">5%</p>
  <p class="stair-value" style="left:600px;top:368px;width:168px">14%</p>
  <p class="stair-value" style="left:768px;top:308px;width:163px">16%</p>
  <p class="stair-value" style="left:931px;top:248px;width:168px">19%</p>
</section>

<section class="band advanced">
  <h2 class="section-title" style="top:26px">4. Are Companies Planning to Use Advanced Methods, Like<br>Deep Learning, Artificial Intelligence and Predictive Models?</h2>
  <svg width="1200" height="564" viewBox="0 0 1200 564">
    <rect x="221" y="192" width="271" height="216" fill="var(--screen)" role="img" aria-label="Computer monitor with a brain symbol"/>
    <rect x="749" y="192" width="271" height="216" fill="var(--screen)" role="img" aria-label="Computer monitor with a brain symbol"/>
    <g stroke="#fff" stroke-width="3" stroke-dasharray="12 8">
      <line x1="255" y1="170" x2="255" y2="420"/>
      <line x1="838" y1="170" x2="838" y2="420"/>
    </g>
  </svg>
  <div class="badge" style="left:169px;top:172px">17%</div>
  <div class="badge" style="left:268px;top:172px">83%</div>
  <div class="badge" style="left:753px;top:172px">40%</div>
  <div class="badge" style="left:849px;top:172px">60%</div>
  <p class="caption" style="left:155px;top:461px;width:400px">17% is already using these methods</p>
  <p class="caption" style="left:668px;top:461px;width:440px">40% expects these methods to be in production within 3 years</p>
</section>

<footer class="band footer">
  <div class="brand" style="left:48px"><span class="brand-mark"></span>Plenvoria</div>
  <div class="brand" style="left:490px">Quarnel Census</div>
  <div class="brand" style="left:880px">Quarnel Fair</div>
</footer>
<div class="band bottom-bar"></div>

</body>
</html>
```